Association qui souhaite améliorer l'accès aux personnes en situation de handicap

Nous sommes une association qui a pour objectif d'améliorer l'accessibilité, augmenter l'offre des activités réalisables dans notre région touristique.
Nous souhaitons réaliser un site internet afin de pouvoir communiquer sur notre association. Nous avons déjà conçu notre flyer sur Graphivolte. Nous souhaiterions une base graphique se rapportant à celui-ci. C'est possible de tout retravailler mais nous souhaitons tout de même retrouver la charte graphique ou code couleur du flyer.
Il nous faudrait quelques pages:
- 1 page : Acceuil / Présentation (Home), Il y aurait le descriptif de l'association, avec ses objectifs à +/- moyen terme
- 1 page : Nos réalisations, celle-ci présenterait les éléments que nous avons réalisés avec des zones de textes et des images classées chronologiquement au fur et à mesure des nouveautés
- 1 page : Media, comme la précédente, mais ou on pourrait voir ou lire sur les divers médias qui parlent de nous
- 1 page : Evenements : c'est une page pour présenter divers activités que nous allons organiser
- 1 page : Contact qui indique comment nous contacter et avec la présentation des 5 ou 6 membres du comité
- 1 link donate : qui arrive sur un formulaire de donnée que l'on pourra faire évoluer sur un système de payement par la suite. Cette bannière doit se retrouver sur toutes les pages
Il est nécessaire que se design puisse être transféré sur une lecture sur téléphone mobile
Personnes en situation de handicap
Associatif
Coded - Design and coding required
5+ page

```html
<!DOCTYPE html>
<html lang="en">
<head>
<meta charset="utf-8">
<title>Openway Association</title>
<link href="https://fonts.googleapis.com/css2?family=Bebas+Neue&family=Raleway:wght@400;500;600;700&display=swap" rel="stylesheet">
<style>
:root{--red:#c1121f;--red-dark:#9e0f19;--ink:#111;--text:#444;--muted:#888;--light:#f2f2f2;--line:#cfcfcf;--dark:#1a1a1a}
*{box-sizing:border-box;margin:0;padding:0}
html,body{width:1200px;height:3705px;overflow:hidden}
body{position:relative;font-family:'Raleway',sans-serif;color:var(--text);background:#fff}
.abs{position:absolute}
.brand{font-family:'Raleway',sans-serif;font-weight:700;font-size:22px;color:var(--ink);display:flex;align-items:center;gap:10px}
.brand i{width:18px;height:18px;background:var(--red);display:inline-block}
.brand.light{color:#fff}
.brand.light i{background:#fff}
.heading{font-family:'Bebas Neue',sans-serif;color:var(--ink);font-weight:400;letter-spacing:.5px}
.heading em{font-style:normal;color:var(--red)}
.bar{height:3px;width:52px;background:var(--red)}
.btn{background:var(--red);color:#fff;font-weight:700;font-size:22px;display:flex;align-items:center;justify-content:center;border-radius:6px;box-shadow:0 4px 10px rgba(0,0,0,.25)}
.photo{border-radius:0}
/* header */
.topbar{top:34px;left:479px;width:610px;height:30px;display:flex;align-items:center;font-size:15px;color:#222;border-bottom:1px solid #999}
.topbar span{margin-right:28px}
.nav{top:84px;left:495px;display:flex;gap:30px;font-size:16px;color:#222}
.nav .active{color:var(--red);font-weight:700;text-decoration:underline}
/* events */
.events{top:1358px;left:0;width:1200px;height:825px;background:linear-gradient(180deg,#1c1c1c,#2a2222 50%,#1a1414)}
.card{width:310px;height:510px;background:#fff;border-radius:6px;overflow:hidden;top:1573px}
.card .img{height:300px}
.card .thumbs{display:flex;height:52px;gap:2px;background:#fff;padding-top:2px}
.card .thumbs div{flex:1}
.card .thumbs .more{background:#111;color:#fff;font-size:11px;display:flex;flex-direction:column;align-items:center;justify-content:center}
.card .thumbs .more b{font-size:20px;line-height:18px}
.card h3{font-size:16px;font-weight:700;color:#111;margin:12px 12px 6px}
.card .date{font-size:10px;color:var(--red);margin:0 14px 8px}
.card p{font-size:11px;line-height:20px;color:#999;margin:0 12px}
.card a{display:block;font-size:14px;font-weight:700;color:#111;text-decoration:underline;margin:10px 12px}
/* achievements */
.award{top:2376px;width:200px;height:108px;background:#fff;border-radius:6px;box-shadow:0 2px 8px rgba(0,0,0,.12);display:flex;align-items:center;justify-content:center}
.award.active{border:2px solid var(--red)}
.award div{width:70px;height:70px;border-radius:50%;background:linear-gradient(135deg,#f4c84a,#d89b22)}
/* contact */
.field{border:1px solid var(--line);height:51px;font-size:12px;color:#999;padding:18px 26px}
.info{display:flex;gap:14px;left:111px}
.info .dot{width:38px;height:38px;border-radius:50%;background:var(--red);display:flex;align-items:center;justify-content:center}
.info h4{font-size:17px;font-weight:500;color:#222}
.info p{font-size:12px;color:#222;line-height:20px}
/* footer */
.foot-h{font-family:'Bebas Neue',sans-serif;color:#fff;font-size:20px}
.foot-list{list-style:none;color:#fff;font-size:15px}
.foot-list li{height:38px;display:flex;align-items:center;gap:14px}
.foot-list li::before{content:"»";font-size:20px;font-weight:700}
.pay{width:56px;height:24px;background:#fff;border-radius:2px;top:3644px}
</style>
</head>
<body>

<!-- hero -->
<div class="abs photo" role="img" aria-label="Three colleagues in a bright office, one seated in a wheelchair" style="top:0;left:0;width:1200px;height:720px;background:linear-gradient(90deg,#fafafa 0%,#f1f1ef 40%,#d9d6cf 65%,#c8c6bf 100%)"></div>
<svg class="abs" style="top:500px;left:0" width="1200" height="260" viewBox="0 0 1200 260">
  <polygon points="0,160 0,260 1200,260 1200,160 720,250" fill="#fff"/>
  <polygon points="0,28 0,48 720,246 700,228" fill="var(--red)"/>
  <polygon points="720,246 1200,100 1200,160 730,250" fill="var(--red)"/>
  <polygon points="0,48 0,60 690,250 720,246" fill="#7a0c14"/>
</svg>

<div class="abs brand" style="top:46px;left:111px"><i></i>OPENWAY ASSOCIATION</div>
<div class="abs topbar">
  <svg width="16" height="16" viewBox="0 0 24 24" style="margin:0 18px 0 14px"><path fill="#222" d="M6.6 10.8a15 15 0 0 0 6.6 6.6l2.2-2.2a1 1 0 0 1 1-.25 11 11 0 0 0 3.6.6 1 1 0 0 1 1 1V20a1 1 0 0 1-1 1A17 17 0 0 1 3 4a1 1 0 0 1 1-1h3.5a1 1 0 0 1 1 1 11 11 0 0 0 .6 3.6 1 1 0 0 1-.25 1z"/></svg>
  <span>Call:+1 555 010 2040</span>
  <svg width="16" height="12" viewBox="0 0 16 12" style="margin-right:28px"><rect width="16" height="12" fill="#222"/><path d="M0 0l8 6 8-6" stroke="#fff" fill="none"/></svg>
  <span>Mail:info@openwayassoc.org</span>
  <span style="margin-right:6px">En</span>
  <svg width="18" height="18" viewBox="0 0 20 20"><circle cx="10" cy="10" r="8" fill="none" stroke="#222" stroke-width="1.5"/><path d="M2 10h16M10 2c3 3 3 13 0 16M10 2c-3 3-3 13 0 16" fill="none" stroke="#222"/></svg>
</div>
<nav class="abs nav"><span class="active">Home</span><span>About</span><span>Our achievements</span><span>Media</span><span>Event</span><span>Contact Us</span>
<svg width="16" height="16" viewBox="0 0 20 20"><circle cx="8" cy="8" r="6" fill="none" stroke="#222" stroke-width="2"/><path d="M13 13l5 5" stroke="#222" stroke-width="2"/></svg></nav>

<h1 class="abs heading" style="top:206px;left:111px;font-size:44px;line-height:52px">WELCOME TO<br><span style="font-size:50px">OPENWAY ASSOCIATION</span></h1>
<p class="abs" style="top:320px;left:111px;width:460px;font-size:13px;line-height:26px;color:#555">Itaque earum rerum hic tenetur a sapiente delectus, ut aut perferendis doloribus asperiores repellat.</p>
<div class="abs btn" style="top:384px;left:111px;width:147px;height:64px">Donate</div>

<!-- media -->
<div class="abs" style="top:867px;left:146px;width:363px;height:405px;border:1.5px solid var(--red)"></div>
<div class="abs photo" role="img" aria-label="Smiling man in a wheelchair with a woman standing behind him at home" style="top:841px;left:111px;width:364px;height:405px;background:linear-gradient(160deg,#d9c7b3,#a8907c 55%,#6d5c55)"></div>
<div class="abs bar" style="top:843px;left:600px"></div>
<h2 class="abs heading" style="top:858px;left:600px;font-size:32px">OUR <em>MEDIA</em></h2>
<div class="abs" style="top:906px;left:600px;width:485px;font-size:14.5px;line-height:28.5px;color:#444">
<p>Nemo enim ipsam voluptatem quia voluptas sit aspernatur aut odit aut fugit, sed quia consuuntur mani dolores eos qui ratione voluatm sequi nesciunt. Neque porro quisquam est, qui dolorem ipsum quia dolor sit amet, consectetur, adipisci velit, sed quia non numquam eius modi tempora incidunt ut labore et dolore magnam aliquam quaerat voluptatem.</p>
<p style="margin-top:28px">Ut enim ad minima veniam, quis nostrum exercitationem ullam corporis suscipit laboriosam, nisi ut aliquid ex ea commodi consequatur.</p>
</div>
<div class="abs btn" style="top:1211px;left:599px;width:163px;height:63px">Read More</div>

<!-- events -->
<section class="abs events" role="img" aria-label="Dark blurred crowd at an event"></section>
<div class="abs bar" style="top:1441px;left:574px;background:#fff"></div>
<h2 class="abs heading" style="top:1456px;left:0;width:1200px;text-align:center;font-size:32px;color:#fff">OUR EVENTS</h2>
<p class="abs" style="top:1508px;left:0;width:1200px;text-align:center;font-size:14.5px;color:#fff">Excepteur sint occaecat cupidatat non proident, sunt in culpa qui officia deserunt mollit anim id est laborum.</p>

<article class="abs card" style="left:111px">
  <div class="img" role="img" aria-label="Group in red costumes gathered around motorbikes in a town square" style="background:linear-gradient(180deg,#9aa39a,#8a2a2a 60%,#3a2a2a)"></div>
  <div class="thumbs"><div style="background:#9a4a44"></div><div style="background:#7a8a6a"></div><div style="background:#8a5a4a"></div><div class="more"><b>+</b>12</div></div>
  <h3>Fugiat Nulla Pariatur</h3><div class="date">Jan 12, 2022</div>
  <p>Quis autem vel eum iure reprehenderit qui in ea voluptate velit esse quam nihil molestiae consequatur</p>
  <a>READ MORE</a>
</article>
<article class="abs card" style="left:445px">
  <div class="img" role="img" aria-label="Man in a red shirt using an adapted outdoor device on a green hillside" style="background:linear-gradient(180deg,#8aa06a,#b04a40 55%,#5a5a50)"></div>
  <div class="thumbs"><div style="background:#6a6a5a"></div><div style="background:#7a9a6a"></div><div style="background:#c9b8a4"></div><div class="more"><b>+</b>6</div></div>
  <h3>Architecto Beatae Vitae</h3><div class="date">Feb 12, 2022</div>
  <p>Excepteur sint occaecat cupidatat non proident, sunt in culpa qui officia deserunt mollit anim id est laborum.</p>
  <a>READ MORE</a>
</article>
<article class="abs card" style="left:778px">
  <div class="img" role="img" aria-label="Man with a white cane walking along a sunny garden path" style="background:linear-gradient(180deg,#b9c79a,#e0956a 45%,#7a8a6a)"></div>
  <div class="thumbs"><div style="background:#8a9a6a"></div><div style="background:#c9a48a"></div><div style="background:#8a6a5a"></div><div class="more"><b>+</b>6</div></div>
  <h3>Ratione Voluptatem Sequi</h3><div class="date">April 12, 2022</div>
  <p>Itaque earum rerum hic tenetur a sapiente delectus, ut aut reiciendis voluptatibus maiores alias consequatur</p>
  <a>READ MORE</a>
</article>

<!-- achievements -->
<section class="abs" style="top:2183px;left:0;width:1200px;height:389px;background:var(--light)"></section>
<div class="abs bar" style="top:2282px;left:574px"></div>
<h2 class="abs heading" style="top:2297px;left:0;width:1200px;text-align:center;font-size:32px">OUR <em>ACHIEVEMENTS</em></h2>
<div class="abs award" style="left:111px"><div></div></div>
<div class="abs award" style="left:369px"><div></div></div>
<div class="abs award active" style="left:627px"><div></div></div>
<div class="abs award" style="left:885px"><div></div></div>

<!-- contact -->
<div class="abs brand" style="top:2660px;left:111px"><i></i>OPENWAY ASSOCIATION</div>
<h2 class="abs heading" style="top:2712px;left:111px;font-size:30px">CONTACT US</h2>
<div class="abs info" style="top:2762px"><div class="dot"><svg width="14" height="18" viewBox="0 0 14 18"><path d="M7 0a7 7 0 0 1 7 7c0 5-7 11-7 11S0 12 0 7a7 7 0 0 1 7-7z" fill="#fff"/><circle cx="7" cy="7" r="2.5" fill="var(--red)"/></svg></div><div><h4>Address</h4><p>Openway Association<br>United States</p></div></div>
<div class="abs info" style="top:2860px"><div class="dot"><svg width="16" height="16" viewBox="0 0 24 24"><path fill="#fff" d="M6.6 10.8a15 15 0 0 0 6.6 6.6l2.2-2.2a1 1 0 0 1 1-.25 11 11 0 0 0 3.6.6 1 1 0 0 1 1 1V20a1 1 0 0 1-1 1A17 17 0 0 1 3 4a1 1 0 0 1 1-1h3.5a1 1 0 0 1 1 1 11 11 0 0 0 .6 3.6 1 1 0 0 1-.25 1z"/></svg></div><div><h4>Phone No</h4><p>+1 555 010 2040</p></div></div>
<div class="abs info" style="top:2920px"><div class="dot"><svg width="16" height="12" viewBox="0 0 16 12"><rect width="16" height="12" fill="#fff"/><path d="M0 0l8 6 8-6" stroke="var(--red)" fill="none"/></svg></div><div><h4>Email</h4><p>info@openwayassoc.org</p></div></div>

<div class="abs field" style="top:2665px;left:459px;width:302px">First Name</div>
<div class="abs field" style="top:2665px;left:785px;width:302px">Last Name</div>
<div class="abs field" style="top:2729px;left:459px;width:302px">Email</div>
<div class="abs field" style="top:2729px;left:785px;width:302px">Phone</div>
<div class="abs field" style="top:2792px;left:459px;width:628px;height:79px">Message</div>
<div class="abs" style="top:2907px;left:460px;width:627px;height:57px;background:var(--red);color:#fff;font-weight:700;font-size:20px;display:flex;align-items:center;justify-content:center">SUBMIT</div>

<!-- footer -->
<svg class="abs" style="top:2980px;left:0" width="1200" height="725" viewBox="0 0 1200 725">
  <polygon points="0,240 480,100 1200,210 1200,725 0,725" fill="#000"/>
  <polygon points="0,150 470,95 0,240" fill="var(--red)"/>
  <polygon points="360,130 1200,195 1200,230 500,150" fill="var(--red)"/>
</svg>
<div class="abs brand light" style="top:3360px;left:111px"><i></i>OPENWAY ASSOCIATION</div>
<p class="abs" style="top:3420px;left:111px;width:310px;color:#fff;font-size:14px;line-height:24px;text-align:justify">Itaque earum rerum hic tenetur a sapiente delectus, ut aut reiciendis voluptatibus maiores alias consequatur aut perferendis doloribus asperiores repellat.</p>

<h3 class="abs foot-h" style="top:3322px;left:475px">QUICK LINKS</h3>
<ul class="abs foot-list" style="top:3364px;left:475px"><li>Home</li><li>Media</li><li>Events</li><li>Achievements</li><li>Contact Us</li></ul>
<h3 class="abs foot-h" style="top:3322px;left:671px">HELP LINKS</h3>
<ul class="abs foot-list" style="top:3357px;left:671px"><li>FAQ</li><li>Terms</li><li>Privacy</li><li>Support</li><li>Conditions</li></ul>
<h3 class="abs foot-h" style="top:3322px;left:841px">CONTACT</h3>
<div class="abs" style="top:3364px;left:841px;color:#fff;font-size:15px;line-height:20px">
  <div style="display:flex;gap:14px"><svg width="20" height="22" viewBox="0 0 14 18"><path d="M7 1a6 6 0 0 1 6 6c0 4-6 10-6 10S1 11 1 7a6 6 0 0 1 6-6z" fill="none" stroke="#fff"/><circle cx="7" cy="7" r="2" fill="none" stroke="#fff"/></svg><span>Openway Association<br>United States</span></div>
  <div style="display:flex;gap:14px;margin-top:14px"><svg width="20" height="14" viewBox="0 0 16 12"><rect x=".5" y=".5" width="15" height="11" fill="none" stroke="#fff"/><path d="M.5.5l7.5 6 7.5-6" stroke="#fff" fill="none"/></svg><span>info@openwayassoc.org</span></div>
  <div style="display:flex;gap:14px;margin-top:30px"><svg width="20" height="20" viewBox="0 0 24 24"><path fill="none" stroke="#fff" stroke-width="1.5" d="M6.6 10.8a15 15 0 0 0 6.6 6.6l2.2-2.2a1 1 0 0 1 1-.25 11 11 0 0 0 3.6.6 1 1 0 0 1 1 1V20a1 1 0 0 1-1 1A17 17 0 0 1 3 4a1 1 0 0 1 1-1h3.5a1 1 0 0 1 1 1 11 11 0 0 0 .6 3.6 1 1 0 0 1-.25 1z"/></svg><span>+1 555 010 2040</span></div>
</div>

<div class="abs" style="top:3604px;left:111px;width:978px;height:1px;background:#555"></div>
<p class="abs" style="top:3645px;left:109px;color:#fff;font-size:15px">Copyrights@2022 Openway Association All Rights Reserved</p>
<div class="abs pay" style="left:774px"></div>
<div class="abs pay" style="left:840px"></div>
<div class="abs pay" style="left:906px"></div>
<div class="abs pay" style="left:972px"></div>
<div class="abs pay" style="left:1030px"></div>

</body>
</html>
```